Professional Business Cards

We need a nice looking, profession and modern business card for our new company. Our logo is attatched

Target Market(s)

Young Professionals

Industry/Entity Type

Financial

Contact Information for Business Card

FRONT

Morvane Tally Pty Ltd
Level 22, Halden Court, 48 Wirrapool St
Sydney NSW 2000
ABN : 57 304 918 226

Derek Wallis - Chief Operations Officer
P : 02 7153 2819
M: 0418 395 207
derek@morvanetally,com

BACK

- Cryptocurrency Exchange Services
- Cryptocurrency Mining Operations
- Cryptocurrency Investment Fund Offering

Font styles to use
Sans Serif

Colors
0255a3
9d9d9d

```html
<!DOCTYPE html>
<html lang="en">
<head>
<meta charset="utf-8">
<title>Morvane Tally – Business Card</title>
<link href="https://fonts.googleapis.com/css2?family=Montserrat:wght@400;500;600&display=swap" rel="stylesheet">
<style>
  :root {
    --backdrop: #2b2c2e;
    --card: #1a1b1d;
    --card-edge: #111214;
    --gloss: #2f3134;
    --accent: #1d9ad8;
    --text: #d9dadb;
    --muted: #9d9d9d;
    --rule: #5a5c60;
  }
  * { margin: 0; padding: 0; box-sizing: border-box; }
  html, body {
    width: 800px; height: 1200px; overflow: hidden;
    background: var(--backdrop);
    font-family: "Montserrat", sans-serif;
  }
  .canvas { position: relative; width: 800px; height: 1200px; }

  .card {
    position: absolute; left: 100px; width: 600px; height: 343px;
    background: var(--card);
    border: 1px solid var(--card-edge);
    box-shadow: 0 18px 40px rgba(0,0,0,.45);
    overflow: hidden;
  }
  .card--front { top: 130px; }
  .card--back { top: 690px; border-top: 5px solid var(--accent); }

  /* Front */
  .front-brand {
    position: absolute; inset: 0;
    display: flex; align-items: center; justify-content: center; gap: 16px;
  }
  .front-brand__square { width: 34px; height: 34px; background: var(--gloss); }
  .front-brand__name {
    font-size: 38px; font-weight: 600; letter-spacing: 3px;
    color: var(--gloss); text-transform: uppercase;
  }

  /* Back */
  .back-brand {
    position: absolute; left: 40px; top: 130px; width: 215px;
    display: flex; flex-direction: column; align-items: center; gap: 14px;
  }
  .back-brand__square { width: 46px; height: 46px; background: var(--accent); }
  .back-brand__name {
    font-size: 22px; font-weight: 600; letter-spacing: 2px;
    color: var(--accent); text-transform: uppercase; text-align: center; line-height: 1.15;
  }
  .divider {
    position: absolute; left: 285px; top: 45px; width: 1px; height: 250px;
    background: var(--rule);
  }
  .details { position: absolute; left: 310px; top: 45px; right: 24px; }
  .person__name {
    font-size: 20px; font-weight: 500; letter-spacing: 3px;
    color: var(--accent); text-transform: uppercase;
  }
  .person__title { font-size: 10px; color: var(--text); margin-top: 3px; }
  .contact { list-style: none; margin-top: 10px; font-size: 11px; line-height: 1.55; color: var(--text); }
  .contact__label { color: var(--accent); font-weight: 600; margin-right: 4px; }
  .company { margin-top: 22px; font-size: 11px; line-height: 1.55; color: var(--text); }
  .company__name { color: var(--accent); font-weight: 600; text-transform: uppercase; letter-spacing: 1px; }
</style>
</head>
<body>
<main class="canvas">

  <section class="card card--front" aria-label="Card front">
    <div class="front-brand">
      <span class="front-brand__square"></span>
      <span class="front-brand__name">Morvane Tally</span>
    </div>
  </section>

  <section class="card card--back" aria-label="Card back">
    <div class="back-brand">
      <span class="back-brand__square"></span>
      <span class="back-brand__name">Morvane Tally</span>
    </div>

    <div class="divider"></div>

    <div class="details">
      <h1 class="person__name">Derek Wallis</h1>
      <p class="person__title">Chief Operating Officer</p>
      <ul class="contact">
        <li><span class="contact__label">P:</span>02 7153 2819</li>
        <li><span class="contact__label">M:</span>0418 395 207</li>
        <li><span class="contact__label">E:</span>derek@morvanetally,com</li>
        <li><span class="contact__label">W:</span>www.morvanetally.com</li>
      </ul>
      <div class="company">
        <p class="company__name">Morvane Tally Pty Ltd</p>
        <p>ABN : 57 304 918 226</p>
        <p>Level 22, Halden Court, 48 Wirrapool St</p>
        <p>Sydney NSW 2000</p>
      </div>
    </div>
  </section>

</main>
</body>
</html>
```